Design a Website Mockup for a custom apparel business

Hello, everyone. I need a website for my custom apparel business. I am not sure how I want my website design so I need a little help.
My business colors are white, black and red.
Page 1 (Homepage) . I want my home page to be similar to this one (http://bramleylensworks.com/) I too much don't care about the bottom of the page but I absolutely love the top of the page. It immediately shows examples of her work, contact information and her social network platforms.
Page 2 (Apparel) . I want to be similar to this page (http://www.qorvanthreadhouse.com/index.php/gear) I like everything about this page except the top of it and I do not offer tie dye shirts.
Page 3 (Graphics). I would like to be a mixture of these two websites (http://www.velmarinkmill.com/ (Need a design?)) I do not like the image on side of the list of things they can do be a do like the list. My list will be Basic, Fashion, School, Sports, Occasions and Work. I also would like something like this (http://www.qorvanthreadhouse.com/index.php/graphics) I like how you click on example of their previous work.
Page 4 (Types of Printing) . I use "heat printing", I use a 'vinyl cutter" and a "screen printer'. I would like information about each printing method and examples of what each method can do. I also want "combinations of methods" that would be like a heat printed image with vinyl letters.
Page 5 (Order form) I want it to be similar to this page (http://www.qorvanthreadhouse.com/index.php/order-form)
Page 6 ( FAQ's )
Page 7 (Contact Us and Live Facebook Feed) I want my contact information at the top and I want a live Facebook feed at the bottom. If you have any question or suggestions please let me know, also PM for my business information. Thank You in advance!

```html
<!DOCTYPE html>
<html lang="en">
<head>
<meta charset="utf-8">
<title>Redloom Wear – Home</title>
<link href="https://fonts.googleapis.com/css2?family=Open+Sans:wght@300;400;600;700&display=swap" rel="stylesheet">
<style>
  :root{
    --page-bg:#1d1d1d;
    --shell-bg:#2b2b2b;
    --header-bg:#2e2e2e;
    --footer-bg:#242424;
    --bottom-bg:#1b1b1b;
    --red:#d0151c;
    --red-dark:#a70f14;
    --white:#ffffff;
    --muted:#bdbdbd;
    --faint:#7d7d7d;
    --card-bg:#ffffff;
    --card-img:#dcdcdc;
    --price:#1a5aa8;
    --social-blue:#2f7fc1;
    --social-green:#3aa34c;
  }
  *{box-sizing:border-box;margin:0;padding:0}
  html,body{width:977px;height:1200px;overflow:hidden}
  body{background:var(--page-bg);font-family:"Open Sans",Arial,sans-serif;color:var(--white);position:relative}
  .shell{position:absolute;left:130px;top:0;width:715px;height:1200px;background:var(--shell-bg)}
  .site-header{position:absolute;left:0;top:0;width:715px;height:123px;background:var(--header-bg)}
  .brand{position:absolute;left:18px;top:50px;font-size:33px;font-weight:300;letter-spacing:.3px;line-height:1;color:var(--white)}
  .shop-hours{position:absolute;right:15px;top:27px;font-size:13.5px;font-weight:700;color:#e0e0e0;text-align:right}
  .shop-address{position:absolute;right:15px;top:45px;font-size:8.5px;color:var(--faint)}
  .call{position:absolute;right:15px;top:59px;font-size:13px;color:#cfcfcf;display:flex;align-items:center;gap:4px}
  .social-top{position:absolute;right:15px;top:87px;display:flex;gap:5px}
  .social-top i{display:block;width:22px;height:22px;border-radius:50%;background:var(--social-blue);border:1px solid #5aa0da}
  .social-top i.mail{background:var(--social-green);border-color:#66c374;display:flex;align-items:center;justify-content:center}
  .main-nav{position:absolute;left:0;top:123px;width:715px;height:34px;background:linear-gradient(#e2232a,var(--red-dark))}
  .main-nav a{color:var(--white);text-decoration:none;font-size:13px;text-transform:uppercase;position:absolute;top:8px}
  .hero{position:absolute;left:0;top:157px;width:715px;height:354px}
  .hero-photo{position:absolute;inset:0;background:linear-gradient(90deg,#8e8f98 0%,#b9ad88 30%,#5e2432 52%,#e9e9ea 62%,#a9a9ab 85%,#efefef 100%)}
  .hero-title{position:absolute;left:68px;top:87px;font-size:40px;font-weight:700;line-height:1;text-shadow:0 2px 4px rgba(0,0,0,.35)}
  .hero-sub{position:absolute;left:68px;top:128px;font-size:32px;font-weight:400;line-height:1.03;text-shadow:0 2px 4px rgba(0,0,0,.35)}
  .btn-learn{position:absolute;left:66px;top:222px;width:105px;height:23px;border-radius:12px;background:linear-gradient(#e0242b,var(--red-dark));font-size:11.5px;font-weight:700;display:flex;align-items:center;padding-left:13px;gap:8px}
  .slide-arrow{position:absolute;top:116px;width:36px;height:36px;border-radius:50%;background:var(--white);display:flex;align-items:center;justify-content:center}
  .slide-arrow.prev{left:11px}
  .slide-arrow.next{right:11px}
  .features{position:absolute;top:573px;left:0;width:715px}
  .feature{position:absolute;width:206px}
  .feature-photo{height:117px;background:linear-gradient(100deg,#f2d23a 0%,#f08a22 25%,#d8261f 45%,#e0417a 65%,#8a3ca3 85%,#4b2f7c 100%)}
  .feature h3{font-size:12.5px;font-weight:400;margin-top:9px}
  .feature p{font-size:9.4px;line-height:13px;color:var(--muted);margin-top:3px}
  .arrivals-title{position:absolute;left:29px;top:812px;font-size:15px;font-weight:400;display:flex;align-items:center;gap:7px}
  .arrivals-title i{width:14px;height:14px;border-radius:50%;background:#e0305a;display:flex;align-items:center;justify-content:center}
  .product{position:absolute;top:846px;width:112px;height:160px;background:var(--card-bg);border:2px solid #e4e4e4;color:#222}
  .product-photo{height:82px;background:radial-gradient(circle at 50% 55%,#5d9ed8 0 30%,var(--card-img) 31%)}
  .product h4{font-size:9.5px;font-weight:600;margin:9px 0 0 6px}
  .product .price{font-size:8.5px;color:#555;margin:10px 0 0 6px}
  .product .price b{color:var(--price)}
  .product-actions{position:absolute;left:6px;bottom:8px;display:flex;align-items:center;gap:3px;width:98px}
  .btn-buy{width:40px;height:12px;border:1px solid #b9c6d6;border-radius:6px;font-size:6.5px;color:#3a6aa0;text-align:center;line-height:10px;margin-right:auto}
  .share{width:11px;height:11px;border-radius:2px;background:#3b64a8}
  .share.t{background:#31a9d8}.share.g{background:#d9534f}
  .site-footer{position:absolute;left:0;top:1052px;width:715px;height:112px;background:var(--footer-bg)}
  .foot-col{position:absolute;top:18px}
  .foot-col h5{font-size:13.5px;font-weight:400;margin-bottom:6px}
  .foot-col p{font-size:10px;color:#cfcfcf;line-height:21px}
  .foot-social{display:flex;gap:20px;margin-top:8px}
  .foot-social i{display:block;width:12px;height:12px;background:#e8e8e8;border-radius:2px}
  .bottom-bar{position:absolute;left:0;top:1164px;width:715px;height:36px;background:var(--bottom-bg);font-size:10px;color:#cfcfcf;padding:11px 0 0 23px}
  .bottom-bar span{color:var(--faint)}
</style>
</head>
<body>
<div class="shell">
  <header class="site-header">
    <div class="brand">REDLOOM WEAR</div>
    <div class="shop-hours">SHOP HOURS: Monday - Friday | 10:00AM - 6:00PM</div>
    <div class="shop-address">418 Harlow Crest, Denmore, TX 75290, USA</div>
    <div class="call">
      <svg width="10" height="10" viewBox="0 0 24 24"><path fill="#9a9a9a" d="M6.6 10.8a15 15 0 006.6 6.6l2.2-2.2a1 1 0 011-.25 11.4 11.4 0 003.6.6 1 1 0 011 1V20a1 1 0 01-1 1A17 17 0 013 4a1 1 0 011-1h3.5a1 1 0 011 1 11.4 11.4 0 00.6 3.6 1 1 0 01-.25 1z"/></svg>
      Call : 555-014-732
    </div>
    <div class="social-top">
      <i></i><i></i><i></i>
      <i class="mail"><svg width="11" height="8" viewBox="0 0 11 8"><rect x=".5" y=".5" width="10" height="7" fill="none" stroke="#fff"/><path d="M.5 .5l5 4 5-4" fill="none" stroke="#fff"/></svg></i>
    </div>
  </header>

  <nav class="main-nav">
    <a href="#" style="left:18px">Home</a>
    <a href="#" style="left:103px">Apparel</a>
    <a href="#" style="left:205px">About</a>
    <a href="#" style="left:293px">Graphics</a>
    <a href="#" style="left:401px">Order Form</a>
    <a href="#" style="left:528px">FAQ's</a>
    <a href="#" style="left:609px">Contact Us</a>
  </nav>

  <section class="hero">
    <div class="hero-photo" role="img" aria-label="Models wearing printed t-shirts beside hooded sweatshirts and printed caps"></div>
    <h1 class="hero-title">CUSTOM APPARELS</h1>
    <p class="hero-sub">BE UNIQUE &amp; SET<br>YOURSELF APART</p>
    <a class="btn-learn">Learn More <svg width="6" height="7" viewBox="0 0 6 7"><path d="M0 0l6 3.5L0 7z" fill="#fff"/></svg></a>
    <div class="slide-arrow prev"><svg width="10" height="16" viewBox="0 0 10 16"><path d="M8 1L2 8l6 7" fill="none" stroke="#444" stroke-width="1.6"/></svg></div>
    <div class="slide-arrow next"><svg width="10" height="16" viewBox="0 0 10 16"><path d="M2 1l6 7-6 7" fill="none" stroke="#444" stroke-width="1.6"/></svg></div>
  </section>

  <section class="features">
    <article class="feature" style="left:25px">
      <div class="feature-photo" role="img" aria-label="Row of colourful shirts on hangers"></div>
      <h3>Custom Apparels</h3>
      <p>Lorem ipsum dolor sit amet, consectetur adipsing elit. Donec mattis consequat massa, a rhoncus nunc facilisis vel. Maecenas tris-tique orci dui.</p>
    </article>
    <article class="feature" style="left:254px">
      <div class="feature-photo" role="img" aria-label="Row of colourful shirts on hangers"></div>
      <h3>Custom Apparels</h3>
      <p>Lorem ipsum dolor sit amet, consectetur adipsing elit. Donec mattis consequat massa, a rhoncus nunc facilisis vel. Maecenas tris-tique orci dui.</p>
    </article>
    <article class="feature" style="left:485px">
      <div class="feature-photo" role="img" aria-label="Row of colourful shirts on hangers"></div>
      <h3>Custom Apparels</h3>
      <p>Lorem ipsum dolor sit amet, consectetur adipsing elit. Donec mattis consequat massa, a rhoncus nunc facilisis vel. Maecenas tris-tique orci dui.</p>
    </article>
  </section>

  <h2 class="arrivals-title"><i><svg width="5" height="7" viewBox="0 0 5 7"><path d="M1 0l3 3.5L1 7" fill="none" stroke="#fff" stroke-width="1.3"/></svg></i>New Arrivals</h2>

  <div class="product" style="left:28px"><div class="product-photo" role="img" aria-label="Light blue t-shirt"></div><h4>Comfort soft tees</h4><p class="price">Price: <b>$23.00</b></p><div class="product-actions"><span class="btn-buy">BUY →</span><i class="share"></i><i class="share t"></i><i class="share g"></i></div></div>
  <div class="product" style="left:158px"><div class="product-photo" role="img" aria-label="Light blue t-shirt"></div><h4>Comfort soft tees</h4><p class="price">Price: <b>$23.00</b></p><div class="product-actions"><span class="btn-buy">BUY →</span><i class="share"></i><i class="share t"></i><i class="share g"></i></div></div>
  <div class="product" style="left:289px"><div class="product-photo" role="img" aria-label="Light blue t-shirt"></div><h4>Comfort soft tees</h4><p class="price">Price: <b>$23.00</b></p><div class="product-actions"><span class="btn-buy">BUY →</span><i class="share"></i><i class="share t"></i><i class="share g"></i></div></div>
  <div class="product" style="left:418px"><div class="product-photo" role="img" aria-label="Light blue t-shirt"></div><h4>Comfort soft tees</h4><p class="price">Price: <b>$23.00</b></p><div class="product-actions"><span class="btn-buy">BUY →</span><i class="share"></i><i class="share t"></i><i class="share g"></i></div></div>
  <div class="product" style="left:548px"><div class="product-photo" role="img" aria-label="Light blue t-shirt"></div><h4>Comfort soft tees</h4><p class="price">Price: <b>$23.00</b></p><div class="product-actions"><span class="btn-buy">BUY →</span><i class="share"></i><i class="share t"></i><i class="share g"></i></div></div>

  <footer class="site-footer">
    <div class="foot-col" style="left:38px">
      <h5>Address</h5>
      <p>B-7, Ashgrove Court<br>Fernwick,<br>London, UK</p>
    </div>
    <div class="foot-col" style="left:241px">
      <h5>Contact</h5>
      <p>hello@redloomwear.com<br>555-018-244<br>F34QL</p>
    </div>
    <div class="foot-col" style="left:535px">
      <h5>Socialize :</h5>
      <div class="foot-social"><i></i><i></i><i></i><i></i></div>
    </div>
  </footer>
  <div class="bottom-bar">Redloom Wear <span>2013 | All rights reseved.</span></div>
</div>
</body>
</html>
```